NEED VIBRANT DIGTAL MENUS

NEED A NEW DESIGN FOR MENU SCREENS

SEE ATTACHED FOR EXISTING MENUS

Requirements
Must have
• FLOW. COLOR. ORGANIZATION. SOPHISTICATION.
Nice to have
• INCORPORATE LOGO IN DESIGNS

```html
<!DOCTYPE html>
<html lang="en">
<head>
<meta charset="utf-8">
<title>Delvano Menu Board</title>
<link rel="stylesheet" href="https://fonts.googleapis.com/css2?family=Oswald:wght@400;600;700&family=Roboto+Condensed:wght@400;700&display=swap">
<style>
  :root {
    --red: #e11d22;
    --red-dark: #b8141a;
    --cream: #fbf4e4;
    --yellow: #f7c51e;
    --green: #2f8d2b;
    --orange: #f29a1d;
    --ink: #2b2220;
    --white: #ffffff;
    --faint: rgba(225, 29, 34, 0.07);
    --bread: #d9a25a;
    --bread-dark: #9a5b24;
  }
  * { box-sizing: border-box; margin: 0; padding: 0; }
  html, body { width: 818px; height: 1200px; overflow: hidden; background: var(--cream); }
  body { font-family: "Roboto Condensed", Arial, sans-serif; color: var(--ink); }
  .menu-board { position: relative; width: 818px; height: 1200px; background: var(--cream); overflow: hidden; }

  .side-band { position: absolute; left: 0; top: 0; width: 56px; height: 1200px; background: var(--red); }
  .side-label {
    position: absolute; left: 0; width: 56px; display: flex; align-items: center; justify-content: center;
  }
  .side-label span {
    transform: rotate(-90deg); white-space: nowrap; color: var(--white);
    font-family: "Oswald", Arial, sans-serif; font-weight: 700; font-size: 34px; letter-spacing: 1px;
  }
  .section-rule { position: absolute; left: 0; height: 3px; background: var(--red); }
  .band-rule { position: absolute; left: 6px; width: 44px; height: 2px; background: var(--white); }

  .brand-title {
    position: absolute; left: 56px; right: 0; top: 14px; text-align: center;
    font-family: "Oswald", Arial, sans-serif; font-weight: 700; font-size: 46px; color: var(--red); letter-spacing: 2px;
  }
  .brand-ghost {
    position: absolute; left: 110px; top: 60px; font-family: "Oswald", Arial, sans-serif; font-weight: 700;
    font-size: 150px; color: var(--faint); letter-spacing: 6px; white-space: nowrap;
  }
  .hours-tag {
    position: absolute; left: 60px; top: 88px; width: 22px; height: 96px; background: var(--orange);
    display: flex; align-items: center; justify-content: center;
  }
  .hours-tag span { transform: rotate(-90deg); white-space: nowrap; color: var(--white); font-size: 10px; font-weight: 700; }

  .item { position: absolute; width: 120px; text-align: center; }
  .item-wide { width: 170px; }
  .price-badge {
    width: 58px; height: 58px; margin: 0 auto; border-radius: 50%; background: var(--red);
    border: 3px solid var(--white); box-shadow: 0 2px 4px rgba(0,0,0,.25);
    display: flex; align-items: center; justify-content: center; position: relative; z-index: 2;
    color: var(--white); font-family: "Oswald", Arial, sans-serif; font-weight: 700; font-size: 17px;
  }
  .food-photo {
    width: 74px; height: 40px; margin: -16px auto 0; border-radius: 50%;
    background: radial-gradient(ellipse at 50% 40%, #f3d27a, var(--bread) 55%, var(--bread-dark));
  }
  .item-name { margin-top: 6px; font-size: 10px; font-weight: 700; text-transform: uppercase; line-height: 1.15; }
  .item-wide .item-name { white-space: nowrap; }

  .section-heading {
    position: absolute; font-family: "Oswald", Arial, sans-serif; font-weight: 700; color: var(--red); font-size: 22px;
  }
  .section-note { position: absolute; font-size: 9px; text-transform: uppercase; }

  .subs-panel { position: absolute; left: 440px; top: 308px; width: 362px; height: 510px; background: var(--yellow); }
  .subs-title {
    position: absolute; left: 0; right: 0; top: 24px; text-align: center; font-family: "Oswald", Arial, sans-serif;
    font-weight: 700; font-size: 42px; color: var(--green);
  }
  .subs-sub { position: absolute; left: 0; right: 0; top: 80px; text-align: center; font-size: 12px; font-weight: 700; }
  .subs-price {
    position: absolute; left: 0; right: 0; top: 98px; text-align: center; color: var(--red);
    font-family: "Oswald", Arial, sans-serif; font-size: 16px; font-weight: 600;
  }
  .sub-item { position: absolute; width: 150px; text-align: center; }
  .sub-photo {
    width: 140px; height: 34px; margin: 0 auto; border-radius: 17px;
    background: linear-gradient(180deg, #e8b36a, var(--bread) 40%, #b9664a 60%, var(--bread-dark));
  }
  .sub-name { margin-top: 5px; font-size: 10px; font-weight: 700; text-transform: uppercase; }
  .steak-band {
    position: absolute; left: 0; right: 0; top: 400px; height: 30px; background: var(--red); color: var(--white);
    text-align: center; font-family: "Oswald", Arial, sans-serif; font-weight: 700; font-size: 20px; line-height: 30px;
  }
  .steak-photo {
    position: absolute; left: 40px; top: 438px; width: 282px; height: 36px; border-radius: 18px;
    background: linear-gradient(180deg, #e8b36a, var(--bread) 40%, #8c5a3a 60%, var(--bread-dark));
  }
  .steak-price {
    position: absolute; left: 0; right: 0; top: 480px; text-align: center; color: var(--ink);
    font-family: "Oswald", Arial, sans-serif; font-size: 15px; font-weight: 600;
  }

  .panini-price { position: absolute; left: 68px; top: 826px; font-family: "Oswald", Arial, sans-serif; font-weight: 700; font-size: 30px; color: var(--red); }
  .panini-heading { position: absolute; left: 160px; top: 832px; font-family: "Oswald", Arial, sans-serif; font-weight: 700; font-size: 17px; color: var(--green); }
  .panini-note { position: absolute; left: 160px; top: 856px; font-size: 10px; font-weight: 700; text-transform: uppercase; }
  .big-badge {
    position: absolute; left: 300px; top: 880px; width: 86px; height: 86px; border-radius: 50%; background: var(--red);
    border: 4px solid var(--white); box-shadow: 0 2px 5px rgba(0,0,0,.25);
    display: flex; align-items: center; justify-content: center; color: var(--white);
    font-family: "Oswald", Arial, sans-serif; font-weight: 700; font-size: 24px; z-index: 2;
  }
  .panini-item { position: absolute; width: 110px; text-align: center; }
  .panini-photo {
    width: 90px; height: 58px; margin: 0 auto; border-radius: 6px;
    background: linear-gradient(135deg, #f1cf83, var(--bread) 50%, var(--bread-dark));
  }

  .sandwich-feature {
    position: absolute; left: 462px; top: 830px; width: 120px; height: 70px; border-radius: 8px;
    background: linear-gradient(135deg, #f1cf83, var(--bread) 50%, var(--bread-dark));
  }
  .sandwich-heading { position: absolute; left: 610px; top: 838px; font-family: "Oswald", Arial, sans-serif; font-weight: 700; font-size: 20px; color: var(--green); }
  .sandwich-note { position: absolute; left: 610px; top: 866px; font-size: 10px; font-weight: 700; text-transform: uppercase; }
  .sandwich-item { position: absolute; width: 110px; text-align: center; }
  .sandwich-price { font-family: "Oswald", Arial, sans-serif; font-weight: 700; font-size: 18px; color: var(--green); }
  .sandwich-photo {
    width: 70px; height: 32px; margin: 2px auto 0; border-radius: 14px;
    background: linear-gradient(180deg, #efc67a, var(--bread) 45%, var(--bread-dark));
  }
</style>
</head>
<body>
<main class="menu-board">
  <div class="brand-ghost" aria-hidden="true">DELVANO</div>

  <div class="side-band"></div>
  <div class="side-label" style="top:80px;height:350px"><span>BREAKFAST</span></div>
  <div class="band-rule" style="top:432px"></div>
  <div class="side-label" style="top:436px;height:380px"><span>LUNCH</span></div>
  <div class="band-rule" style="top:816px"></div>
  <div class="side-label" style="top:820px;height:380px"><span>LUNCH</span></div>

  <div class="section-rule" style="top:432px;left:56px;width:384px"></div>
  <div class="section-rule" style="top:816px;left:56px;width:762px"></div>

  <h1 class="brand-title">DELVANO</h1>
  <div class="hours-tag"><span>UNTIL 10:30AM</span></div>

  <section class="breakfast">
    <div class="item" style="left:110px;top:176px"><div class="price-badge">$4.59</div><div class="food-photo" role="img" aria-label="Bacon, egg and cheese sandwich"></div><p class="item-name">Bacon, Egg &amp; Cheese</p></div>
    <div class="item" style="left:240px;top:176px"><div class="price-badge">$4.59</div><div class="food-photo" role="img" aria-label="Sausage, egg and cheese sandwich"></div><p class="item-name">Sausage, Egg &amp; Cheese</p></div>
    <div class="item" style="left:420px;top:176px"><div class="price-badge">$5.49</div><div class="food-photo" role="img" aria-label="Ham, egg and cheese sandwich"></div><p class="item-name">Ham, Egg &amp; Cheese</p></div>
    <div class="item" style="left:560px;top:176px"><div class="price-badge">$5.99</div><div class="food-photo" role="img" aria-label="Bologna, egg and cheese sandwich"></div><p class="item-name">Bologna, Egg &amp; Cheese</p></div>
    <div class="item" style="left:110px;top:316px"><div class="price-badge">$6.99</div><div class="food-photo" role="img" aria-label="Chicken, egg and cheese sandwich"></div><p class="item-name">Chicken, Egg &amp; Cheese</p></div>
    <div class="item" style="left:240px;top:316px"><div class="price-badge">$7.99</div><div class="food-photo" role="img" aria-label="Steak, egg and cheese sandwich"></div><p class="item-name">Steak, Egg &amp; Cheese</p></div>
  </section>

  <section class="burgers">
    <h2 class="section-heading" style="left:76px;top:440px">HANDCRAFTED BURGERS</h2>
    <p class="section-note" style="left:76px;top:472px">All burgers are 100% hand made patties</p>
    <div class="item item-wide" style="left:86px;top:492px"><div class="price-badge">$6.49</div><div class="food-photo" role="img" aria-label="Quarter pound cheeseburger"></div><p class="item-name">1/4LB Cheeseburger</p></div>
    <div class="item item-wide" style="left:260px;top:492px"><div class="price-badge">$8.49</div><div class="food-photo" role="img" aria-label="Half pound super cheeseburger"></div><p class="item-name">1/2LB Super Cheeseburger</p></div>
    <div class="item item-wide" style="left:86px;top:598px"><div class="price-badge">$7.49</div><div class="food-photo" role="img" aria-label="Quarter pound bacon cheeseburger"></div><p class="item-name">1/4LB Bacon Cheeseburger</p></div>
    <div class="item item-wide" style="left:260px;top:598px"><div class="price-badge">$9.99</div><div class="food-photo" role="img" aria-label="Half pound bacon super cheeseburger"></div><p class="item-name">1/2LB Bacon Super Cheeseburger</p></div>
    <div class="item item-wide" style="left:86px;top:704px"><div class="price-badge">$7.99</div><div class="food-photo" role="img" aria-label="Bologna burger"></div><p class="item-name">Bologna Burger</p></div>
    <div class="item item-wide" style="left:260px;top:704px"><div class="price-badge">$9.99</div><div class="food-photo" role="img" aria-label="Super bologna burger"></div><p class="item-name">Super Bologna Burger</p></div>
  </section>

  <section class="subs-panel">
    <h2 class="subs-title">SUPER SUBS</h2>
    <p class="subs-sub">SERVED ON FRESH BAKED ROLLS</p>
    <p class="subs-price">Half $12.99 &nbsp; Whole $17.99</p>
    <div class="sub-item" style="left:18px;top:126px"><div class="sub-photo" role="img" aria-label="Ham and cheese sub"></div><p class="sub-name">Ham &amp; Cheese</p></div>
    <div class="sub-item" style="left:194px;top:126px"><div class="sub-photo" role="img" aria-label="Oven roasted chicken sub"></div><p class="sub-name">Oven Roasted Chicken</p></div>
    <div class="sub-item" style="left:18px;top:214px"><div class="sub-photo" role="img" aria-label="Italian sub"></div><p class="sub-name">Italian</p></div>
    <div class="sub-item" style="left:194px;top:214px"><div class="sub-photo" role="img" aria-label="Combo sub"></div><p class="sub-name">Combo</p></div>
    <div class="sub-item" style="left:18px;top:302px"><div class="sub-photo" role="img" aria-label="Cajun sub"></div><p class="sub-name">Cajun</p></div>
    <div class="sub-item" style="left:194px;top:302px"><div class="sub-photo" role="img" aria-label="Roast beef sub"></div><p class="sub-name">Roast Beef</p></div>
    <div class="steak-band">STEAK CHEESE</div>
    <div class="steak-photo" role="img" aria-label="Steak and cheese sub"></div>
    <p class="steak-price">Half $11.99 &nbsp; Whole $21.99</p>
  </section>

  <section class="paninis">
    <p class="panini-price">$7.99</p>
    <h2 class="panini-heading">FRESH GRILLED PANINIS</h2>
    <p class="panini-note">served with chips</p>
    <div class="big-badge">$8.99</div>
    <div class="panini-item" style="left:66px;top:900px"><div class="panini-photo" role="img" aria-label="Turkey melt panini"></div><p class="item-name">Turkey Melt</p></div>
    <div class="panini-item" style="left:180px;top:900px"><div class="panini-photo" role="img" aria-label="Italian panini"></div><p class="item-name">Italian</p></div>
    <div class="panini-item" style="left:66px;top:1000px"><div class="panini-photo" role="img" aria-label="Chicken pesto panini"></div><p class="item-name">Chicken Pesto</p></div>
    <div class="panini-item" style="left:180px;top:1000px"><div class="panini-photo" role="img" aria-label="Ham and swiss panini"></div><p class="item-name">Ham &amp; Swiss</p></div>
    <div class="panini-item" style="left:294px;top:1000px"><div class="panini-photo" role="img" aria-label="Veggie panini"></div><p class="item-name">Veggie</p></div>
    <div class="panini-item" style="left:180px;top:1100px"><div class="panini-photo" role="img" aria-label="Buffalo chicken panini"></div><p class="item-name">Buffalo Chicken</p></div>
  </section>

  <section class="sandwiches">
    <div class="sandwich-feature" role="img" aria-label="Grilled sandwich with chips"></div>
    <h2 class="sandwich-heading">SANDWICHES</h2>
    <p class="sandwich-note">served with chips</p>
    <div class="sandwich-item" style="left:456px;top:918px"><p class="sandwich-price">$7.99</p><div class="sandwich-photo" role="img" aria-label="Turkey club sandwich"></div><p class="item-name">Turkey Club</p></div>
    <div class="sandwich-item" style="left:570px;top:918px"><p class="sandwich-price">$7.99</p><div class="sandwich-photo" role="img" aria-label="Ham and cheese sandwich"></div><p class="item-name">Ham &amp; Cheese</p></div>
    <div class="sandwich-item" style="left:684px;top:918px"><p class="sandwich-price">$8.99</p><div class="sandwich-photo" role="img" aria-label="Italian sandwich"></div><p class="item-name">Italian</p></div>
    <div class="sandwich-item" style="left:456px;top:1010px"><p class="sandwich-price">$7.99</p><div class="sandwich-photo" role="img" aria-label="Chicken salad sandwich"></div><p class="item-name">Chicken Salad</p></div>
    <div class="sandwich-item" style="left:570px;top:1010px"><p class="sandwich-price">$5.99</p><div class="sandwich-photo" role="img" aria-label="BLT sandwich"></div><p class="item-name">BLT</p></div>
    <div class="sandwich-item" style="left:684px;top:1010px"><p class="sandwich-price">$8.99</p><div class="sandwich-photo" role="img" aria-label="Cheesesteak sandwich"></div><p class="item-name">Cheesesteak</p></div>
    <div class="sandwich-item" style="left:456px;top:1110px"><div class="sandwich-photo" role="img" aria-label="Country ham sandwich"></div><p class="item-name">Country Ham</p></div>
    <div class="sandwich-item" style="left:570px;top:1110px"><div class="sandwich-photo" role="img" aria-label="Tuna melt sandwich"></div><p class="item-name">Tuna Melt</p></div>
    <div class="sandwich-item" style="left:684px;top:1110px"><div class="sandwich-photo" role="img" aria-label="Club sandwich"></div><p class="item-name">Club</p></div>
  </section>
</main>
</body>
</html>
```